Magazine Insert Redesign for Industrial Machinery Manufacturer

Corvimax Ltd rely on publishing inserts in industrial magazines across the UK. Our inserts introduce our key products on one page; they show the concept of the product, include some key points about the functions of the machine, and show examples of installations.Our leaflet is now a little dated, and we would like to revise the design. The attached files give more information. Please review our briefing document.

Target Market(s)

Engineers, business owners, production managers

Industry/Entity Type

Manufacturing

Colors

Designer to choose colors to be used in the design.

Requirements
Must have
• Our new logo
• A look in line with branding guidelines

```html
<!DOCTYPE html>
<html lang="en">
<head>
<meta charset="utf-8">
<title>Corvimax Insert</title>
<link href="https://fonts.googleapis.com/css2?family=Fira+Sans:wght@400;600;800&family=Oswald:wght@500;600&display=swap" rel="stylesheet">
<style>
  :root {
    --backdrop: #efefef;
    --sky: #66b4dd;
    --stone: #d4d4d6;
    --forest: #096c34;
    --forest-deep: #05572a;
    --leaf: #4fae6c;
    --teal: #2fa596;
    --white: #ffffff;
    --steel: #b9bcc0;
  }
  * { box-sizing: border-box; margin: 0; padding: 0; }
  html, body { width: 1200px; height: 816px; overflow: hidden; background: var(--backdrop); }
  body { font-family: "Fira Sans", Arial, sans-serif; }
  .insert {
    position: absolute; left: 320px; top: 18px; width: 560px; height: 780px;
    background: var(--stone); overflow: hidden;
    box-shadow: 0 6px 24px rgba(0,0,0,.12);
  }
  .insert__sky { position: absolute; left: 0; top: 0; }
  .headline {
    position: absolute; left: 34px; top: 58px; color: var(--white);
    font-weight: 800; font-size: 29px; line-height: 1.08; letter-spacing: -0.3px;
  }
  .brand {
    position: absolute; left: 378px; top: 176px; display: flex; align-items: center; gap: 8px;
    color: var(--forest); font-weight: 800; font-size: 28px;
  }
  .brand__dot { width: 14px; height: 14px; border-radius: 50%; background: var(--teal); }
  .insert__ground {
    position: absolute; left: 0; top: 400px; width: 560px; height: 380px;
    background: linear-gradient(180deg, var(--forest-deep), var(--forest) 40%);
  }
  .hero {
    position: absolute; left: 100px; top: 238px; width: 360px; height: 290px;
    border-radius: 6px;
    background:
      radial-gradient(ellipse at 25% 30%, rgba(47,165,150,.75), rgba(47,165,150,0) 55%),
      radial-gradient(ellipse at 80% 45%, rgba(79,174,108,.8), rgba(79,174,108,0) 55%),
      linear-gradient(160deg, #e4e5e7, var(--steel));
  }
  .hero__label {
    position: absolute; font-family: "Oswald", "Arial Narrow", sans-serif; font-weight: 600;
    color: var(--white); text-transform: uppercase; line-height: 1.05; text-align: center;
  }
  .hero__label--dust { left: 40px; top: 58px; font-size: 22px; }
  .hero__label--clean { left: 232px; top: 110px; font-size: 32px; }
  .features {
    position: absolute; left: 18px; top: 548px; width: 524px; height: 92px;
    display: grid; grid-template-columns: repeat(5, 1fr);
  }
  .feature {
    display: flex; flex-direction: column; align-items: center; gap: 6px;
    padding: 0 8px; color: var(--white); font-size: 9.5px; font-weight: 400; line-height: 1.25; text-align: center;
  }
  .feature + .feature { border-left: 1px solid rgba(255,255,255,.35); }
  .feature svg { width: 22px; height: 22px; }
  .gallery {
    position: absolute; left: 0; top: 646px; width: 560px; height: 134px; display: flex;
    clip-path: polygon(0 22px, 100% 0, 100% 100%, 0 100%);
  }
  .gallery__photo { height: 100%; }
  .gallery__photo--bench { width: 200px; background: linear-gradient(135deg, #8b8e93, #c9c2b8 60%, #5f6670); }
  .gallery__photo--lab { width: 190px; background: linear-gradient(135deg, #d9d3c7, #f1ede6 50%, #a79c8c); }
  .gallery__photo--sander { width: 170px; background: linear-gradient(135deg, #e6e6e6, #9a7a6e 55%, #6c6f58); }
  .contact { position: absolute; left: 0; top: 746px; }
  .contact__text {
    position: absolute; left: 0; top: 746px; width: 560px; height: 34px;
    display: flex; align-items: center; justify-content: flex-end; padding-right: 22px; gap: 8px;
    color: var(--forest-deep); font-weight: 600; font-size: 11px;
  }
</style>
</head>
<body>
<main class="insert">
  <svg class="insert__sky" width="560" height="260" viewBox="0 0 560 260" aria-hidden="true">
    <path d="M0 0 H560 V30 C430 150 220 220 0 240 Z" fill="var(--sky)"/>
  </svg>
  <h1 class="headline">Plug in. Switch on.<br>Dust and fumes? All gone.<br>Really, it's that simple.</h1>

  <div class="brand"><span class="brand__dot"></span>Corvimax</div>

  <div class="insert__ground"></div>

  <div class="hero" role="img" aria-label="Grey downdraught extraction bench with curved arrows showing dust and fumes drawn in and clean air returned">
    <span class="hero__label hero__label--dust">Dust &amp;<br>Fumes</span>
    <span class="hero__label hero__label--clean">Clean<br>Air</span>
  </div>

  <section class="features">
    <div class="feature">
      <svg viewBox="0 0 24 24"><path d="M4 6h14v3H4z M8 11h10v3H8z" fill="#fff"/><circle cx="8" cy="19" r="2" fill="#fff"/><circle cx="15" cy="19" r="2" fill="#fff"/></svg>
      Takes dust and fumes away from your breathing zone
    </div>
    <div class="feature">
      <svg viewBox="0 0 24 24"><rect x="3" y="5" width="18" height="4" fill="#fff"/><rect x="4" y="10" width="16" height="10" fill="none" stroke="#fff" stroke-width="2"/></svg>
      Draws them through the worksurface, capturing them inside the bench
    </div>
    <div class="feature">
      <svg viewBox="0 0 24 24"><rect x="3" y="11" width="10" height="10" fill="#fff"/><path d="M21 3 L14 10 M14 5 V10 H19" stroke="#fff" stroke-width="2" fill="none"/></svg>
      Is available in a wide range of sizes and filter configurations to suit your application
    </div>
    <div class="feature">
      <svg viewBox="0 0 24 24"><path d="M6 8h12v5a6 6 0 0 1-12 0z M9 3v5 M15 3v5 M12 19v3" stroke="#fff" stroke-width="2" fill="#fff"/></svg>
      Is plug &amp; go - only needing unwrapping and plugging in to a 13 amp socket
    </div>
    <div class="feature">
      <svg viewBox="0 0 24 24"><rect x="4" y="4" width="16" height="3" fill="#fff"/><rect x="5" y="8" width="14" height="13" fill="none" stroke="#fff" stroke-width="2"/><path d="M9 10v9 M12 10v9 M15 10v9" stroke="#fff" stroke-width="1.5"/></svg>
      You get extraction and work bench in one compact unit
    </div>
  </section>

  <div class="gallery">
    <div class="gallery__photo gallery__photo--bench" role="img" aria-label="Workshop with extraction benches and tool boards"></div>
    <div class="gallery__photo gallery__photo--lab" role="img" aria-label="Technician in protective suit working at an extraction bench"></div>
    <div class="gallery__photo gallery__photo--sander" role="img" aria-label="Operator sanding a part on a downdraught bench"></div>
  </div>

  <svg class="contact" width="560" height="34" viewBox="0 0 560 34" aria-hidden="true">
    <path d="M220 34 C232 10 240 4 262 4 H560 V34 Z" fill="var(--sky)"/>
  </svg>
  <footer class="contact__text">
    <span>www.corvimax-air.co.uk</span><span>•</span>
    <span>T. 01632 960418</span><span>•</span>
    <span>E. sales@corvimax-air.co.uk</span>
  </footer>
</main>
</body>
</html>
```